Thermlio Energy Ratings Whole Home Energy Rating Flyer

Please create a flyer 8.5" x 11" that is 2-sided that goes hand and hand with my tri-fold flyer. The flyer will target prospective homeowners and real estate agents to purchase a whole home energy rating. I have attached further details.

Target Market(s)

Homeowners looking to remodel their homes, save on energy bills, purchase or sell a home.

Font styles to use
Serif
Sans Serif

Colors
3176b5
ffffff

Requirements
Must have
• Must be able to sell a whole home energy rating on its own!
Nice to have
• I would like to mimic the colors and background of my tri-fold flyer.
Should not have
• Should not be boring!

```html
<!DOCTYPE html>
<html lang="en">
<head>
<meta charset="utf-8">
<title>Thermlio Energy Ratings – Whole Home Energy Rating Flyer</title>
<link href="https://fonts.googleapis.com/css2?family=Montserrat:wght@400;600;700;800&family=Open+Sans:wght@400;600&display=swap" rel="stylesheet">
<style>
:root{
  --brand-blue:#3176b5;
  --bright-blue:#1f86e0;
  --navy:#1d2a3a;
  --panel:#3c3c3f;
  --panel-dark:#222224;
  --ink:#2a2a2a;
  --white:#ffffff;
  --muted:#d4d4d6;
  --stage:#3a3a3a;
}
*{box-sizing:border-box;margin:0;padding:0}
html,body{width:791px;height:1200px;overflow:hidden;background:var(--stage)}
body{position:relative;font-family:"Open Sans",Arial,sans-serif;color:var(--white)}
.page{position:absolute;left:175px;width:440px;height:570px;background:var(--panel);overflow:hidden;box-shadow:0 2px 8px rgba(0,0,0,.45)}
.page--front{top:12px}
.page--back{top:618px}
.shapes{position:absolute;inset:0;width:440px;height:570px}
.art{position:absolute}
.house-art{left:12px;top:30px;width:205px;height:200px;border-radius:4px;
  background:linear-gradient(160deg,#f4f1ec 0%,#d9d2c8 45%,#7fbf4a 62%,#f2c230 74%,#e2412f 90%)}
.solar-photo{left:0;top:0;width:440px;height:250px;
  background:linear-gradient(180deg,#4f8fd8 0%,#a9c9ea 35%,#2b4f8c 60%,#6b5a4c 100%)}
.logo{position:absolute;left:250px;top:24px;font-family:"Montserrat",sans-serif;font-weight:800;color:var(--navy);font-size:25px;letter-spacing:.5px;line-height:1}
.logo-sub{position:absolute;left:330px;top:51px;font-family:"Montserrat",sans-serif;font-weight:600;font-size:6.5px;color:var(--brand-blue);letter-spacing:.4px}
.pitch{position:absolute;left:247px;top:82px;width:185px;font-family:"Montserrat",sans-serif;text-transform:uppercase;font-size:8.2px;line-height:11px}
.pitch .ask{color:var(--bright-blue);font-weight:600}
.pitch .answer{color:var(--ink)}
.col{position:absolute;font-size:5.1px;line-height:6.6px;color:var(--muted)}
.col h2{font-family:"Montserrat",sans-serif;text-transform:uppercase;color:var(--white);font-size:8.5px;line-height:10px;font-weight:400;margin-bottom:3px}
.col h2 b{font-weight:700;display:block}
.col p{margin-bottom:5px}
.col .lead{color:var(--white);font-size:6px;line-height:7.5px}
.ticks{list-style:none;display:grid;grid-template-columns:repeat(3,1fr);gap:1px 6px;font-size:4.6px;line-height:5.6px}
.ticks li{padding-left:6px;position:relative}
.ticks li::before{content:"";position:absolute;left:0;top:1.5px;width:3px;height:2px;border-left:1px solid var(--bright-blue);border-bottom:1px solid var(--bright-blue);transform:rotate(-45deg)}
.bullets{list-style:none}
.bullets li{padding-left:7px;position:relative;margin-bottom:5px}
.bullets li::before{content:"";position:absolute;left:0;top:2px;width:3px;height:2px;border-left:1px solid var(--bright-blue);border-bottom:1px solid var(--bright-blue);transform:rotate(-45deg)}
.call-box{position:absolute;left:236px;top:467px;width:140px;height:46px;border:1px solid var(--white);text-align:center;font-family:"Montserrat",sans-serif;font-weight:700;line-height:15px;padding-top:8px}
.call-box .label{font-size:13px;display:block}
.call-box .phone{font-size:13px;display:block}
.call-icon{position:absolute;left:300px;top:460px;width:13px;height:13px}
.site{position:absolute;right:22px;bottom:7px;font-family:"Montserrat",sans-serif;font-weight:700;font-size:10.5px}
.reviews{position:absolute;left:18px;top:326px;width:404px;height:134px;background:var(--panel-dark);padding:7px 14px;font-size:5.2px;line-height:6.7px;color:var(--muted)}
.reviews h3{font-family:"Montserrat",sans-serif;text-align:center;color:var(--white);font-size:8px;margin-bottom:6px;letter-spacing:.3px}
.reviews p{margin-bottom:7px}
.reviews .by{display:block;text-align:right;color:var(--white);padding-right:20px}
.google-note{position:absolute;left:20px;top:467px;width:400px;text-align:center;font-size:6.4px;line-height:8.4px}
.footer-note{position:absolute;left:30px;bottom:7px;width:380px;text-align:center;text-transform:uppercase;font-size:4.8px;line-height:6.2px;color:var(--white)}
</style>
</head>
<body>

<section class="page page--front" aria-label="Flyer front">
  <svg class="shapes" viewBox="0 0 440 570" aria-hidden="true">
    <rect width="440" height="250" fill="#ffffff"/>
    <polygon points="0,262 300,222 355,238 440,205 440,570 0,570" fill="#3c3c3f"/>
    <polygon points="0,250 300,200 440,165 440,205 355,238 300,222 0,262" fill="#1f86e0"/>
    <polygon points="0,562 170,548 440,520 440,570 0,570" fill="#1f86e0"/>
  </svg>
  <div class="art house-art" role="img" aria-label="3D cutaway house illustration with a colour-coded energy rating scale from green A to red G"></div>

  <div class="logo">THERMLIO</div>
  <div class="logo-sub">ENERGY RATINGS</div>

  <div class="pitch">
    <p class="ask">Would you like to lower your monthly energy bill, enjoy a safer, more comfortable and durable home, and increase your homes appraisal value and sales appeal?</p>
    <p class="answer">Then keep reading, because that is what a lost cost, home energy rating can do for you...</p>
  </div>

  <div class="col" style="left:18px;top:272px;width:195px">
    <h2>What is a <b>Whole Home Energy Rating?</b></h2>
    <p>A Whole Home Energy Rating is a comprehensive evaluation of the efficiency of the entire home. You will receive a written report that includes a numeric score or "rating" of the home, plus recommendations for improvements that will reduce energy bills and make the home more comfortable. Each rating will receive an official California Home Energy Rating Certificate and home energy rating report with the California Energy Commission's (CEC) seal. The report will identify the most cost-effective and appropriate energy efficiency improvements needed to save you money and provide long lasting comfort.</p>
    <h2 style="margin-top:8px">Who <b>Performs the Rating?</b></h2>
    <p>A Home Energy Rating System (HERS) Rater, who is certified by the CEC will conduct the rating. Each California HERS Rater must follow standardized energy auditing procedures and use energy analysis software that meets CEC requirements.</p>
    <p class="lead">The HERS Rater will inspect and assess all the major energy efficiency features of your home:</p>
    <ul class="ticks">
      <li>Air leaks</li><li>Water heating system</li><li>Major appliances</li>
      <li>Cooling system</li><li>Windows</li><li>Solar (if any)</li>
      <li>Heating system</li><li>Lighting</li><li>Other energy uses</li>
      <li>Cooling/heating duct system</li><li>Insulation (attic, walls, floor, roof)</li><li>Prior energy bills</li>
    </ul>
  </div>

  <div class="col" style="left:232px;top:272px;width:192px">
    <h2>Who needs a <b>Whole Home Energy Rating?</b></h2>
    <p>Everyone! Whether you are buying or selling, or plan on staying in your home for one year or the rest of your life, each whole home energy rating is geared toward helping you save money, and is custom tailored to fit your unique needs. The whole home energy rating can be designed to fit any lifestyle or energy improvement budget, with a focal point on cost effectiveness and common sense.</p>
    <p>Buyers who choose to get a whole home energy rating can better decide which home will save them money through energy efficiency! They may also be entitled to federal tax credits, and borrow up to $40,000 for energy improvements through their mortgage.</p>
    <p>Sellers who have a CEC certificate showing their homes energy efficiency ultimately make their homes more valuable and often sell their homes faster than those without documentation.</p>
    <p>Before you remodel your home, make sure you have a HERS Rater conduct a Whole Home Energy Rating so you know exactly where to focus your money.</p>
  </div>

  <svg class="call-icon" viewBox="0 0 14 14" aria-hidden="true">
    <circle cx="7" cy="7" r="7" fill="#1f86e0"/>
    <path d="M4.6 3.6l1.4-.3.7 1.7-.9.6a5 5 0 0 0 2.3 2.3l.6-.9 1.7.7-.3 1.4c-3 .2-5.7-2.5-5.5-5.5z" fill="#ffffff"/>
  </svg>
  <div class="call-box"><span class="label">CALL TODAY</span><span class="phone">(555) 014-2270</span></div>
  <div class="site">www.ThermlioRatings.com</div>
</section>

<section class="page page--back" aria-label="Flyer back">
  <div class="art solar-photo" role="img" aria-label="Photo of a technician installing solar panels on a home roof under a blue sky"></div>
  <svg class="shapes" viewBox="0 0 440 570" aria-hidden="true">
    <polygon points="0,250 260,215 440,165 440,230 0,250" fill="#ffffff"/>
    <polygon points="0,250 440,230 440,570 0,570" fill="#3c3c3f"/>
    <polygon points="0,528 440,512 440,570 0,570" fill="#1f86e0"/>
  </svg>

  <div class="col" style="left:20px;top:258px;width:190px">
    <ul class="bullets">
      <li>Every report is custom tailored to each unique home.</li>
      <li>Thermlio Energy Ratings includes a free duct leakage test and free building envelope leakage test with each home energy audit.</li>
      <li>Heating and cooling ducts in an average California home leak almost 30 percent. That is why when heating or cooling equipment is replaced, testing the system's ducts for leaks is now required by building officials in many parts of the state.</li>
    </ul>
  </div>
  <div class="col" style="left:230px;top:258px;width:192px">
    <ul class="bullets">
      <li>You wouldn't buy a new car without knowing the "miles per gallon", so why buy a home without knowing the "home energy rating?"</li>
      <li>After your mortgage payment, your energy bill is often the second largest monthly home ownership expense.</li>
      <li>Combine an Energy Efficient Mortgage (EEM) with other programs and you may be able to borrow up to $40,000 or more for efficiency improvements. Ask a knowledgeable lender if an EEM is right for you.</li>
    </ul>
  </div>

  <div class="reviews">
    <h3>CUSTOMER REVIEWS:</h3>
    <p>"I had the pleasure of hiring Thermlio to perform a home energy audit on my home and I was truly amazed by the level of professionalism and the great service I received from Dan Orwell. The audit report he provided me was very complete and informative. It allowed me to make informed financial decision regarding repairs to my home. After providing me the report he call me to explain everything in it and suggested various item to make my home more energy efficient. Mr. Orwell is a wealth of knowledge and I will highly recommend it to any homeowner." <span class="by">- Martin L.</span></p>
    <p>"While having my air conditioning replaced, my contractor called this company to do the duct test. Mr. Orwell arrived right on time, and explained the process thoroughly. He was clean and efficient while working throughout the house. He put my mind at ease during the process. I would definitely recommend this company." <span class="by">- Helen R.</span></p>
  </div>

  <p class="google-note">Google "w hole home energy ratings California" for details on w hat I am targeting.<br>http://brightcoilenergy.example/energy-audits/ is a website that somewhat offers what I do</p>

  <p class="footer-note">Please be creative! The verbage I have outlined above is for reference only and does not have to be exact. If you think something can be better worded or get the point across with less, then by all means go right ahead. This is directed at homeowners to purchase an energy rating, so this needs to be geared toward selling the product.</p>
</section>

</body>
</html>
```